ONE PAGE WEB DESIGN NEEDED for Finance Company

We need a web design (ONE PAGE DESIGN ONLY) for a new finance website called Brightwell Lending. Brightwell Lending helps customers get the right loan, whether its a home loan, investment loan, business loan etc.

You are required to come up with just the homepage design. Professionalism and quality is the key factors in the successful design.

Here are a few design questions to help you out:

-
What information should be used on the page?
Ive provided a document which outlines all the information needed to put on homepage (attached to the brief - called brightwell_page_info). Also see the Must Have section below on this brief.

-
What links should appear in the navigation/footer?:
The navigation should provide links to the following pages (NOTE: services link has subcategories):
1 Homepage
2 Services
- Home loans
- Investment loans
- Refinancing loans
- Business loans
3 About Us
4 FAQ
5 Contact Us

-
What colors should be used in the design?
Our company colors - Cyan: #2EADE3, Blue: #004B70, White. Feel free to submit designs with slight variations if you feel it improves the design.

-
What should the layout of the page be?
This is up to you to come up with - we are open to different layouts for the page design (as long as they capture the information effectively and making it easy to understand).

Target Market(s)

Potential Home owners, Families and Business Owners

Industry/Entity Type

Business

Requirements
Must have
• - Must contain our logo (attached as PNG and Illustrator file)
- Winning designer must supply a Photoshop file (PSD) that will allow us.
Nice to have
• - Should include photos/images of families, professional groups, tradespeople etc (you can use stock photos from PixQuarry and I will purchase them once you are selected as the winning design)
- Link to a loan calculator somewhere on front page with a button 'Find out how much you could borrow' (or maybe even try adding a loan calculator to the homepage if you think this would look good)
- Page should have a main headline "Finding the right loan for you" or "Brightwell Lending finds the right loan for our customers."
- Must include Accreditation logos somewhere on the homepage (will try and supply these soon)
Should not have
• - Poor quality designs will not be considered
- Do not use clipart

```html
<!DOCTYPE html>
<html lang="en">
<head>
<meta charset="utf-8">
<title>Brightwell Lending</title>
<link rel="stylesheet" href="https://fonts.googleapis.com/css2?family=Open+Sans:wght@400;600;700&family=Roboto+Condensed:wght@400&family=Tinos:wght@400;700&display=swap">
<style>
  :root {
    --cyan: #2eade3;
    --cyan-bar: #1eaee6;
    --blue: #004b70;
    --link: #2f9fdc;
    --ink: #555555;
    --ink-soft: #7a7a7a;
    --page-bg: #e8e8e8;
    --sheet: #ffffff;
    --rule: #9a9a9a;
  }
  * { box-sizing: border-box; margin: 0; padding: 0; }
  html, body { width: 1200px; height: 1102px; overflow: hidden; }
  body { background: var(--page-bg); position: relative; font-family: "Open Sans", sans-serif; color: var(--ink); }
  .sheet { position: absolute; left: 50px; top: 27px; width: 1100px; height: 1044px; background: var(--sheet); }
  .abs { position: absolute; }

  .brand { left: 101px; top: 66px; display: flex; flex-direction: column; align-items: flex-start; }
  .brand-dot { width: 44px; height: 44px; border-radius: 50%; background: var(--cyan); margin-left: 58px; margin-bottom: 10px; }
  .brand-name { font-size: 23px; font-weight: 600; color: var(--blue); letter-spacing: -0.3px; }

  .call { right: 94px; top: 47px; font-family: "Roboto Condensed", sans-serif; font-size: 27px; color: #8a8a8a; }
  .call span { color: var(--cyan); }

  .nav { left: 86px; top: 162px; width: 1032px; height: 37px; background: var(--cyan-bar); }
  .nav a { position: absolute; top: 9px; font-family: "Roboto Condensed", sans-serif; font-size: 15px; color: #fff; text-decoration: none; }
  .search { position: absolute; left: 813px; top: 6px; width: 208px; height: 26px; background: #fff; }
  .search span { position: absolute; left: 8px; top: 5px; font-family: "Roboto Condensed", sans-serif; font-size: 12.5px; color: #9a9a9a; }
  .search svg { position: absolute; right: 9px; top: 5px; }

  .hero { left: 89px; top: 204px; width: 1029px; height: 250px; background: linear-gradient(90deg, #9a9a9a 0%, #d8d8d8 18%, #6c6c6c 40%, #a9a9a9 60%, #3f3f3f 80%, #5a5a5a 100%); }

  .feature { top: 482px; width: 230px; }
  .feature h3 { font-size: 18.5px; font-weight: 400; line-height: 24px; color: #444; text-transform: uppercase; letter-spacing: -0.2px; }
  .feature .icon { position: absolute; left: 197px; top: 2px; width: 28px; height: 28px; background: #eaeaea; border-radius: 3px; display: flex; align-items: center; justify-content: center; box-shadow: inset 0 -1px 0 #d0d0d0; }
  .feature h4 { margin-top: 16px; font-size: 16.5px; font-weight: 400; color: #555; white-space: nowrap; }
  .body-copy { font-family: "Tinos", serif; font-size: 12.5px; line-height: 22px; color: var(--ink-soft); }
  .feature .body-copy { margin-top: 2px; width: 220px; }
  .more { font-family: "Tinos", serif; font-weight: 700; font-size: 13px; color: var(--link); text-decoration: underline; }
  .feature .more { position: absolute; top: 170px; left: 0; }

  .rule { left: 86px; width: 1031px; border-top: 2px dotted var(--rule); }

  .welcome-photo { left: 83px; top: 743px; width: 197px; height: 175px; background: linear-gradient(160deg, #d6d6d6 0%, #f2f2f2 45%, #8c8c8c 80%, #2e2e2e 100%); }
  .welcome { left: 297px; top: 740px; width: 545px; }
  .welcome h2 { font-size: 19.5px; font-weight: 400; color: #444; text-transform: uppercase; letter-spacing: -0.2px; }
  .welcome .body-copy { margin-top: 14px; }
  .welcome .body-copy b, .welcome .body-copy em { color: var(--link); font-style: normal; }
  .welcome .more { display: inline-block; margin-top: 18px; }

  .quote { left: 897px; top: 800px; width: 207px; height: 54px; background: linear-gradient(#3dbcef, #56c6f3); border: 1px solid #2a9fd6; color: #fff; font-weight: 700; font-size: 22px; text-align: center; line-height: 50px; letter-spacing: 0.3px; text-decoration: none; }

  .copyright { left: 88px; top: 1027px; font-family: "Roboto Condensed", sans-serif; font-size: 13.5px; color: #8a8a8a; }
</style>
</head>
<body>
  <div class="sheet"></div>

  <header>
    <div class="abs brand">
      <div class="brand-dot"></div>
      <div class="brand-name">Brightwell Lending</div>
    </div>
    <div class="abs call">Call: <span>555-0142-789</span></div>

    <nav class="abs nav">
      <a style="left:39px" href="#">HOME</a>
      <a style="left:125px" href="#">ABOUT</a>
      <a style="left:217px" href="#">SERVICES</a>
      <a style="left:327px" href="#">FAQ</a>
      <a style="left:401px" href="#">CONTACT US</a>
      <div class="search">
        <span>SEARCH</span>
        <svg width="16" height="16" viewBox="0 0 16 16"><circle cx="6.5" cy="6.5" r="4.5" fill="none" stroke="#999" stroke-width="2"/><line x1="10" y1="10" x2="14.5" y2="14.5" stroke="#999" stroke-width="2.5" stroke-linecap="round"/></svg>
      </div>
    </nav>
  </header>

  <div class="abs hero" role="img" aria-label="Black and white photo of a smiling team of loan advisers in an office"></div>

  <section class="services">
    <div class="abs feature" style="left:90px">
      <h3>Home<br>Loans</h3>
      <div class="icon"><svg width="18" height="18" viewBox="0 0 20 20"><polygon points="10,1 12.6,7 19,7.4 14,11.6 15.6,18 10,14.5 4.4,18 6,11.6 1,7.4 7.4,7" fill="#777"/></svg></div>
      <h4>Buy the home you want</h4>
      <p class="body-copy">Compare rates from trusted lenders and find a home loan that suits your budget and family.</p>
      <a class="more" href="#">Read More</a>
    </div>
    <div class="abs feature" style="left:357px">
      <h3>Investment<br>Loans</h3>
      <div class="icon"><svg width="20" height="20" viewBox="0 0 20 20"><circle cx="10" cy="10" r="8.5" fill="none" stroke="#777" stroke-width="1.8"/><circle cx="10" cy="10" r="5" fill="none" stroke="#777" stroke-width="1.8"/><circle cx="10" cy="10" r="2" fill="#777"/></svg></div>
      <h4>Grow your property portfolio</h4>
      <p class="body-copy">Flexible finance for your next investment property, with repayments planned around your goals.</p>
      <a class="more" href="#">Read More</a>
    </div>
    <div class="abs feature" style="left:624px">
      <h3>Refinancing<br>Loans</h3>
      <div class="icon"><svg width="14" height="20" viewBox="0 0 14 20"><path d="M7 1a6 6 0 0 0-3.5 10.9V14h7v-2.1A6 6 0 0 0 7 1z" fill="#777"/><rect x="4" y="15" width="6" height="1.8" fill="#777"/><rect x="4.8" y="17.6" width="4.4" height="1.6" fill="#777"/></svg></div>
      <h4>Lower your repayments</h4>
      <p class="body-copy">Switch to a better rate or combine your debts into one simple loan with a lower monthly cost.</p>
      <a class="more" href="#">Read More</a>
    </div>
    <div class="abs feature" style="left:892px">
      <h3>Business<br>Loans</h3>
      <div class="icon"><svg width="18" height="18" viewBox="0 0 18 18"><circle cx="6.5" cy="6.5" r="4.5" fill="none" stroke="#777" stroke-width="2"/><line x1="10" y1="10" x2="16" y2="16" stroke="#777" stroke-width="3" stroke-linecap="round"/></svg></div>
      <h4>Fund your next step</h4>
      <p class="body-copy">Finance for equipment, vehicles, premises or cash flow, so your business can keep moving.</p>
      <a class="more" href="#">Read More</a>
    </div>
  </section>

  <div class="abs rule" style="top:706px"></div>

  <section>
    <div class="abs welcome-photo" role="img" aria-label="Photo of a bright modern family lounge with a white sofa and framed art"></div>
    <div class="abs welcome">
      <h2>Finding the right loan for you</h2>
      <p class="body-copy"><b>Brightwell Lending finds the right loan for our customers.</b> Whether you are buying your first home, growing an investment portfolio, refinancing or funding a business, our brokers compare lenders for you and explain every option in plain terms. <em>Find out how much you could borrow</em> with our quick loan calculator today.</p>
      <a class="more" href="#">Read More</a>
    </div>
    <a class="abs quote" href="#">get a quote</a>
  </section>

  <div class="abs rule" style="top:1010px"></div>
  <footer class="abs copyright">Copyright 2102 Brightwell Lending .com</footer>
</body>
</html>
```